Travel Agency Website - Simple General

Need a 7 page simple design that is pretty repetitive. Need to be able to load quickly that is SEO optimized. Trying to give ideas on what they can do, be personal as we are local, but at the same time come across as professional and get information easily with little burden.

- Landing Page
- Brambleton Vacations Page
- Family Trips
- Road Trips from Texas
- Other Destinations
- About Us Page
- Contact Us Page

Target Market(s)

Families

Coding

Coded - Design and coding required

Number of Pages Required

5+ page

Colors

Designer to choose colors to be used in the design.

Requirements
Must have
• Like it to flow easily with our logo. Use that for colors, etc.

```html
<!DOCTYPE html>
<html lang="en">
<head>
<meta charset="utf-8">
<title>Meander Lane Travel Co. — Enjoy Your Vacations</title>
<link rel="stylesheet" href="https://fonts.googleapis.com/css2?family=Cookie&family=Montserrat:wght@400;600&display=swap">
<style>
:root{
  --teal:#1d4f5c;
  --teal-dark:#163c47;
  --gold:#b48a35;
  --green:#4e6b55;
  --footer:#233a42;
  --ink:#2a2a2a;
  --line:#d9d9d9;
  --white:#ffffff;
}
*{margin:0;padding:0;box-sizing:border-box}
html,body{width:1200px;height:2349px;overflow:hidden;background:var(--white)}
body{position:relative;font-family:'Montserrat',sans-serif;color:var(--ink)}

/* header */
.site-header{position:absolute;left:0;top:0;width:1200px;height:62px;background:var(--white);z-index:5}
.main-nav a{position:absolute;top:18px;font-family:'Cookie',cursive;font-size:22px;color:var(--teal);text-decoration:none}
.main-nav a.active{color:var(--gold);text-decoration:underline}
.icon-btn{position:absolute;top:17px;width:28px;height:28px;border-radius:50%;background:var(--teal)}
.icon-btn svg{position:absolute;left:7px;top:7px}
.estimate-btn{position:absolute;left:1005px;top:16px;width:132px;height:31px;border-radius:16px;background:var(--teal);color:var(--white);font-family:'Cookie',cursive;font-size:21px;text-align:center;line-height:31px}
.brand-badge{position:absolute;left:528px;top:10px;width:144px;height:144px;border-radius:50%;background:var(--white);box-shadow:0 4px 14px rgba(0,0,0,.15);z-index:6;display:flex;align-items:center;justify-content:center;text-align:center;font-family:'Cookie',cursive;font-size:34px;line-height:30px;color:var(--teal)}

/* hero */
.hero{position:absolute;left:0;top:62px;width:1200px;height:570px;overflow:hidden}
.hero-photo{position:absolute;inset:0;background:linear-gradient(110deg,#7a4a2c 0%,#c9785a 25%,#5b6f9a 45%,#9fb8d8 60%,#c8952e 80%,#6b5a4a 100%)}
.hero-shade{position:absolute;inset:0;background:rgba(0,0,0,.18)}
.hero-kicker{position:absolute;left:0;width:1200px;top:195px;text-align:center;font-family:'Cookie',cursive;font-size:36px;color:#e3b64d}
.hero-title{position:absolute;left:0;width:1200px;top:222px;text-align:center;font-family:'Cookie',cursive;font-weight:400;font-size:130px;color:var(--white);line-height:1}
.hero-wave{position:absolute;left:0;top:420px;display:block}

/* tour cards */
.tour-card{position:absolute;top:711px;width:250px}
.tour-photo{width:250px;height:262px;border-radius:4px}
.tour-label{position:absolute;left:19px;top:248px;width:212px;height:52px;background:var(--white);border-radius:4px 4px 0 0;box-shadow:0 10px 14px -8px rgba(0,0,0,.12);text-align:center;font-family:'Cookie',cursive;font-size:27px;line-height:48px;color:var(--teal)}

/* about */
.about{position:absolute;left:0;top:1077px;width:1200px;height:437px;overflow:hidden}
.about-left{position:absolute;left:0;top:0;width:600px;height:437px;background:linear-gradient(160deg,#6d5a92 0%,#2a2f6b 45%,#1a1f4a 100%)}
.about-right{position:absolute;left:600px;top:0;width:600px;height:437px;background:linear-gradient(170deg,#b7a9a0 0%,#9b6a4a 50%,#3a2a2a 100%)}
.about-panel{position:absolute;left:398px;top:0}
.about-copy{position:absolute;left:452px;top:88px;width:296px;text-align:center}
.about-copy h2{font-family:'Cookie',cursive;font-weight:400;font-size:40px;color:var(--gold);margin-bottom:12px;line-height:1}
.about-copy p{font-size:11.6px;line-height:13.8px;margin-bottom:20px}
.pill-btn{display:inline-block;width:93px;height:31px;border-radius:16px;background:var(--teal);color:var(--white);font-family:'Cookie',cursive;font-size:20px;line-height:31px;text-align:center}

/* inquiry */
.inquiry-title{position:absolute;left:0;width:1200px;top:1590px;text-align:center;font-family:'Cookie',cursive;font-weight:400;font-size:42px;color:var(--gold)}
.field{position:absolute;height:34px;border:1px solid var(--line);border-radius:2px;font-size:10.5px;color:#9a9a9a;padding:11px 12px}
.field.message{height:79px;padding-top:10px}
.submit-btn{position:absolute;left:564px;top:1867px;width:72px;height:30px;border-radius:15px;background:var(--teal);color:var(--white);font-family:'Cookie',cursive;font-size:20px;line-height:30px;text-align:center}

/* footer */
.site-footer{position:absolute;left:0;top:2060px;width:1200px;height:256px;background:var(--footer)}
.footer-wave{position:absolute;left:0;top:1960px;display:block}
.footer-badge{position:absolute;left:160px;top:2135px;width:140px;height:130px;border-radius:50%;background:var(--white);display:flex;align-items:center;justify-content:center;text-align:center;font-family:'Cookie',cursive;font-size:32px;line-height:28px;color:var(--teal)}
.footer-col{position:absolute;top:2140px;color:var(--white);font-size:12.2px}
.footer-col h3{font-family:'Cookie',cursive;font-weight:400;font-size:26px;color:var(--gold);margin-bottom:6px;line-height:1.1}
.footer-col li{list-style:none;line-height:22px}
.contact-row{display:flex;gap:8px;line-height:16px;margin-bottom:9px}
.contact-row svg{flex:none;margin-top:2px}
.legal-bar{position:absolute;left:0;top:2316px;width:1200px;height:33px;background:var(--teal-dark)}
.legal-bar p{position:absolute;left:154px;top:10px;font-size:10.5px;color:var(--white)}
.social-dot{position:absolute;top:9px;width:15px;height:15px;border-radius:50%;background:var(--white)}
</style>
</head>
<body>

<header class="site-header">
  <nav class="main-nav">
    <a class="active" style="left:63px">Home</a>
    <a style="left:128px">Tours</a>
    <a style="left:190px">About Us</a>
    <a style="left:271px">Contact Us</a>
  </nav>
  <span class="icon-btn" style="left:926px"><svg width="14" height="14" viewBox="0 0 14 14"><rect x="1" y="3" width="12" height="8" rx="1" fill="#fff"/><path d="M1 3l6 5 6-5" stroke="#1d4f5c" fill="none"/></svg></span>
  <span class="icon-btn" style="left:962px"><svg width="14" height="14" viewBox="0 0 14 14"><path d="M3 1l2 3-1 1.5c1 2 2.5 3.5 4.5 4.5L10 9l3 2-1 2C6 13 1 8 1 2z" fill="#fff"/></svg></span>
  <span class="estimate-btn">Get A Free Estimate</span>
</header>
<div class="brand-badge">Meander<br>Lane</div>

<section class="hero">
  <div class="hero-photo" role="img" aria-label="Excited family riding a theme park coaster in front of a fairytale castle"></div>
  <div class="hero-shade"></div>
  <p class="hero-kicker">Enjoy Your</p>
  <h1 class="hero-title">Vacations</h1>
  <svg class="hero-wave" width="1200" height="150" viewBox="0 0 1200 150">
    <defs><linearGradient id="heroBand" x1="0" x2="1"><stop offset="0" stop-color="#4e6b55"/><stop offset="0.55" stop-color="#5d6e4f"/><stop offset="1" stop-color="#b48a35"/></linearGradient></defs>
    <path d="M0 82 C140 42 300 42 430 72 C560 104 650 108 780 76 C920 40 1060 8 1200 14 L1200 150 L0 150Z" fill="url(#heroBand)"/>
    <path d="M0 100 C150 64 310 64 440 96 C570 130 660 132 790 100 C930 64 1060 38 1200 44 L1200 150 L0 150Z" fill="#fff"/>
  </svg>
</section>

<article class="tour-card" style="left:72px">
  <div class="tour-photo" role="img" aria-label="Brambleton resort castle lit up at dusk" style="background:linear-gradient(180deg,#b9aaa6,#8a5a48 60%,#3e2a26)"></div>
  <div class="tour-label">Brambleton Vacations</div>
</article>
<article class="tour-card" style="left:341px">
  <div class="tour-photo" role="img" aria-label="Happy family on a seaside pier" style="background:linear-gradient(180deg,#9fbfd8,#6a6470 55%,#2d2a30)"></div>
  <div class="tour-label">Family Trips</div>
</article>
<article class="tour-card" style="left:609px">
  <div class="tour-photo" role="img" aria-label="Yellow camper van on a desert road past red cliffs" style="background:linear-gradient(180deg,#9a4a36,#c7956a 50%,#a9a69c)"></div>
  <div class="tour-label">Texas Road Trips</div>
</article>
<article class="tour-card" style="left:878px">
  <div class="tour-photo" role="img" aria-label="Family hiking through a green forest" style="background:linear-gradient(180deg,#6f9a3e,#9bb56a 45%,#4d6a46)"></div>
  <div class="tour-label">Other Destinations</div>
</article>

<section class="about">
  <div class="about-left" role="img" aria-label="Cruise ship lit with purple lights at dusk"></div>
  <div class="about-right" role="img" aria-label="Illuminated resort castle at sunset"></div>
  <svg class="about-panel" width="404" height="437" viewBox="0 0 404 437">
    <path d="M202 0 C230 30 265 40 305 40 C340 45 375 70 378 115 C380 150 390 180 404 218 C390 256 380 286 378 322 C375 367 340 392 305 397 C265 397 230 407 202 437 C174 407 139 397 99 397 C64 392 29 367 26 322 C24 286 14 256 0 218 C14 180 24 150 26 115 C29 70 64 45 99 40 C139 40 174 30 202 0Z" fill="#fff"/>
  </svg>
  <div class="about-copy">
    <h2>About Us</h2>
    <p>Lorem Ipsum Is Simply Dummy Text Of The Printing And Typesetting Industry. Lorem Ipsum Has Been The Industry's Standard Dummy Text Ever Since The 1500s, When An Unknown Printer Took A Galley Of Type And Scrambled It To Make A Type Specimen Book.</p>
    <p>It Has Survived Not Only Five Centuries, But Also The Leap Into Electronic Typesetting, Remaining Essentially Unchanged.</p>
    <span class="pill-btn">Read More</span>
  </div>
</section>

<h2 class="inquiry-title">Quick Inquiry</h2>
<form>
  <div class="field" style="left:325px;top:1656px;width:269px">First Name</div>
  <div class="field" style="left:607px;top:1656px;width:268px">Last Name</div>
  <div class="field" style="left:325px;top:1705px;width:269px">Email</div>
  <div class="field" style="left:607px;top:1705px;width:268px">Phone</div>
  <div class="field message" style="left:325px;top:1755px;width:550px">How Can We Help?</div>
  <span class="submit-btn">Submit</span>
</form>

<footer class="site-footer" role="img" aria-label="Faded theme park castle backdrop"></footer>
<svg class="footer-wave" width="1200" height="110" viewBox="0 0 1200 110">
  <defs><linearGradient id="footBand" x1="0" x2="1"><stop offset="0" stop-color="#b48a35"/><stop offset="0.5" stop-color="#7a7440"/><stop offset="1" stop-color="#4e6b55"/></linearGradient></defs>
  <path d="M0 106 C200 100 350 72 480 42 C600 14 720 8 850 28 C1000 52 1100 44 1200 26 L1200 110 L0 110Z" fill="url(#footBand)"/>
  <path d="M0 110 L0 108 C220 104 370 90 500 66 C620 42 740 38 870 56 C1010 76 1100 68 1200 52 L1200 110Z" fill="#233a42"/>
</svg>
<div class="footer-badge">Meander<br>Lane</div>

<div class="footer-col" style="left:381px">
  <h3>Contact Us</h3>
  <div class="contact-row"><svg width="12" height="12" viewBox="0 0 14 14"><path d="M3 1l2 3-1 1.5c1 2 2.5 3.5 4.5 4.5L10 9l3 2-1 2C6 13 1 8 1 2z" fill="#b48a35"/></svg>(08) 5550 1274</div>
  <div class="contact-row"><svg width="12" height="12" viewBox="0 0 14 14"><rect x="1" y="3" width="12" height="9" rx="1" fill="#b48a35"/><path d="M1 3l6 5 6-5" stroke="#233a42" fill="none"/></svg>hello@meanderlanetravel.com</div>
  <div class="contact-row"><svg width="12" height="14" viewBox="0 0 12 14"><path d="M6 0a5 5 0 015 5c0 4-5 9-5 9S1 9 1 5a5 5 0 015-5z" fill="#b48a35"/><circle cx="6" cy="5" r="2" fill="#233a42"/></svg>Unit 7, 12 Harbour Row,<br>Eastvale, Western Australia, 6001</div>
</div>
<div class="footer-col" style="left:676px">
  <h3>Tours</h3>
  <ul><li>Brambleton Vacations</li><li>Family Trips</li><li>Road Trips From Texas</li><li>Other Destinations</li></ul>
</div>
<div class="footer-col" style="left:885px">
  <h3>Quick Links</h3>
  <ul><li>Home</li><li>About Us</li><li>Contact Us</li></ul>
</div>

<div class="legal-bar">
  <p>© 2026 <strong>Meander Lane,</strong> All Rights Reserved.</p>
  <span class="social-dot" style="left:1000px"></span>
  <span class="social-dot" style="left:1026px"></span>
</div>

</body>
</html>
```